Header Card Design for Marine Tool Product

We package up our small tools in bags. A nice header card would finish the look.
* Bag is 4" wide. Header Card should be 4x4, folded to 4x2
* Back of card should have 2.25x1.25 area for our part number sticker.
* Design to reinforce the brand and add (perception of) quality to the product.

Brand Website: keelworks.net

Target Market(s)

Boat Mechanics/Boat owners

Industry/Entity Type

```html
<!DOCTYPE html>
<html lang="en">
<head>
<meta charset="utf-8">
<title>Keelworks Header Card</title>
<link href="https://fonts.googleapis.com/css2?family=Montserrat:wght@800&family=Poppins:wght@600&family=Mrs+Saint+Delafield&family=Arimo&display=swap" rel="stylesheet">
<style>
  :root {
    --ink: #033a47;
    --teal: #3b6776;
    --teal-deep: #2a5a68;
    --orange: #d4692f;
    --white: #ffffff;
    --grey-line: #8c8c8c;
    --label-grey: #9a9a9a;
  }
  * { margin: 0; padding: 0; box-sizing: border-box; }
  html, body { width: 1200px; height: 1200px; overflow: hidden; background: var(--white); }
  .sheet { position: relative; width: 1200px; height: 1200px; }

  .card {
    position: absolute; left: 120px; width: 960px; height: 481px;
    border: 1.5px solid var(--grey-line); background: var(--white); overflow: hidden;
  }
  .card--front { top: 80px; }
  .card--back { top: 638px; }

  .hang-hole {
    position: absolute; width: 48px; height: 48px; border-radius: 50%;
    border: 1.5px solid var(--grey-line); background: var(--white); z-index: 3;
  }
  .card--front .hang-hole { left: 456px; top: 23px; }
  .card--back .hang-hole { left: 464px; top: 24px; }

  .brand-mark { position: absolute; background: var(--teal); }
  .brand-name {
    position: absolute; font-family: "Montserrat", sans-serif; font-weight: 800;
    color: var(--ink); line-height: 1; white-space: nowrap;
  }
  .card--front .brand-mark { left: 114px; top: 82px; width: 190px; height: 190px; }
  .card--front .brand-name { left: 356px; top: 137px; font-size: 76px; }

  .wave { position: absolute; left: 0; top: 0; width: 960px; height: 481px; }
  .tagline {
    position: absolute; left: 80px; top: 378px; width: 820px; text-align: center;
    font-family: "Mrs Saint Delafield", cursive; font-size: 70px; color: var(--white);
    transform: rotate(-3deg); white-space: nowrap;
  }

  .card--back .brand-mark { left: 22px; top: 40px; width: 118px; height: 118px; }
  .card--back .brand-name { left: 168px; top: 72px; font-size: 52px; }
  .part-label {
    position: absolute; left: 28px; bottom: 10px;
    font-family: "Arimo", sans-serif; font-size: 29px; color: var(--label-grey);
  }

  .info-panel {
    position: absolute; left: 540px; top: 0; width: 420px; height: 481px;
    background: linear-gradient(160deg, var(--teal) 0%, var(--teal-deep) 100%);
  }
  .badge-shield {
    position: absolute; left: 28px; top: 26px; width: 186px; height: 128px;
    background: var(--white); border-radius: 24px 24px 60px 60px;
  }
  .badge-shield::after {
    content: ""; position: absolute; inset: 6px; background: #1d2a5c;
    border-radius: 20px 20px 56px 56px;
  }
  .badge-seal {
    position: absolute; left: 230px; top: 20px; width: 150px; height: 150px;
    border-radius: 50%; background: #1f4652; border: 8px solid var(--orange);
  }
  .contact {
    position: absolute; left: 30px; top: 208px; list-style: none;
    font-family: "Poppins", sans-serif; font-weight: 600; font-size: 28px;
    color: var(--white); line-height: 40px;
  }
  .contact li { display: flex; align-items: flex-start; gap: 10px; }
  .contact li + li { margin-top: 8px; }
  .contact svg { flex: none; width: 24px; height: 24px; margin-top: 8px; fill: var(--white); }
</style>
</head>
<body>
<div class="sheet">

  <section class="card card--front">
    <span class="hang-hole"></span>
    <span class="brand-mark"></span>
    <span class="brand-name">KEELWORKS</span>
    <svg class="wave" viewBox="0 0 960 481" preserveAspectRatio="none">
      <path d="M0 318 C120 380 300 395 480 360 C640 328 800 300 960 308 L960 481 L0 481 Z" fill="var(--orange)"/>
      <path d="M0 330 C120 392 300 405 480 370 C640 338 800 312 960 322 L960 481 L0 481 Z" fill="var(--teal-deep)"/>
      <path d="M0 350 C140 405 320 410 500 382 C660 358 820 340 960 350 L960 481 L0 481 Z" fill="var(--teal)"/>
    </svg>
    <p class="tagline">Born in Charleston, South Carolina</p>
  </section>

  <section class="card card--back">
    <span class="hang-hole"></span>
    <span class="brand-mark"></span>
    <span class="brand-name">KEELWORKS</span>
    <p class="part-label">AMT0006 - 32mm x S-4mm Pins</p>

    <div class="info-panel" role="img" aria-label="Faint nautical chart pattern with compasses and ships">
      <span class="badge-shield" role="img" aria-label="Established badge"></span>
      <span class="badge-seal" role="img" aria-label="Lifetime warranty seal"></span>
      <ul class="contact">
        <li>
          <svg viewBox="0 0 24 24"><path d="M12 2a7 7 0 0 0-7 7c0 5 7 13 7 13s7-8 7-13a7 7 0 0 0-7-7zm0 9.5A2.5 2.5 0 1 1 12 6.5a2.5 2.5 0 0 1 0 5z"/></svg>
          <span>418 Harbor View Rd,<br>Suite 110,<br>Charleston SC,<br>29412</span>
        </li>
        <li>
          <svg viewBox="0 0 24 24"><path d="M6.6 10.8a15.1 15.1 0 0 0 6.6 6.6l2.2-2.2a1 1 0 0 1 1-.25 11.4 11.4 0 0 0 3.6.57 1 1 0 0 1 1 1V20a1 1 0 0 1-1 1A17 17 0 0 1 3 4a1 1 0 0 1 1-1h3.5a1 1 0 0 1 1 1c0 1.25.2 2.45.57 3.57a1 1 0 0 1-.25 1z"/></svg>
          <span>(843)555-0172</span>
        </li>
        <li>
          <svg viewBox="0 0 24 24" fill="none" stroke="#fff" stroke-width="1.8" style="fill:none"><circle cx="12" cy="12" r="10"/><ellipse cx="12" cy="12" rx="4.5" ry="10"/><path d="M2 12h20M4 6.5h16M4 17.5h16"/></svg>
          <span>www.keelworks.net</span>
        </li>
      </ul>
    </div>
  </section>

</div>
</body>
</html>
```